Flyer for family counseling

For my family counseling I'm looking for a design for flyers. Important is not only the appearance of the flyer, but also the content design. All important contents can be found on my website: www.brigitte-volkanter.at The following items should NOT appear on the flyer: - constellation work - bereavement and palliative work My logo should definitely be on the flyer. Source files are available.

Target Market(s)

Families, individuals, children, couples in need of psychological support.

Colors

Designer to choose colors to be used in the design.

Requirements
Must have
• My logo - source files available Website and contact data Recognition value from website to flyer and vice versa
Should not have
• Mention of the constellation work and mourning and palliative work not desired.

```html
<!DOCTYPE html>
<html lang="en">
<head>
<meta charset="utf-8">
<title>Familienberatung Donaufeld – Flyer</title>
<link rel="stylesheet" href="https://fonts.googleapis.com/css2?family=Tinos:ital,wght@0,400;0,700;1,400&display=swap">
<style>
  :root {
    --teal: #179e9b;
    --teal-light: #3fc0bb;
    --blue: #1b70bb;
    --blue-dark: #1560a6;
    --blue-head: #1f7cc4;
    --sky: #d6eef9;
    --ink: #111a22;
    --white: #ffffff;
    --stage: #dcdcdc;
  }
  * { box-sizing: border-box; margin: 0; padding: 0; }
  html, body { width: 1200px; height: 2586px; overflow: hidden; }
  body {
    background: var(--stage);
    font-family: "Tinos", "Times New Roman", serif;
    color: var(--ink);
    position: relative;
  }
  .flyer {
    position: absolute;
    left: 0; top: 445px;
    width: 1200px; height: 1696px;
    overflow: hidden;
    background: var(--sky);
  }
  .flyer-backdrop { position: absolute; inset: 0; width: 1200px; height: 1696px; }
  .brand {
    position: absolute; left: 150px; top: 110px; width: 220px;
    text-align: center; color: var(--teal); font-weight: 400;
  }
  .brand-dot {
    width: 96px; height: 96px; border-radius: 50%;
    background: var(--teal); margin: 0 auto 16px;
  }
  .brand-name { font-size: 22px; letter-spacing: 1px; text-transform: uppercase; white-space: nowrap; }
  .brand-tag { font-size: 15px; letter-spacing: 5px; text-transform: uppercase; white-space: nowrap; margin-top: 4px; margin-left: -60px; margin-right: -60px; }
  .headline {
    position: absolute; left: 50px; top: 520px;
    font-size: 72px; line-height: 62px; font-weight: 400;
    color: var(--teal); text-transform: uppercase; white-space: nowrap;
  }
  .lead {
    position: absolute; left: 50px; top: 738px; width: 560px;
    font-size: 26px; line-height: 31px;
  }
  .section-title {
    position: absolute; left: 50px;
    color: var(--blue-head); font-weight: 700;
  }
  .about-title { top: 872px; font-size: 31px; }
  .about-text { position: absolute; left: 50px; top: 916px; width: 545px; font-size: 24px; line-height: 29px; }
  .respect-title { top: 1058px; width: 540px; font-size: 28px; line-height: 32px; }
  .topics-intro { position: absolute; left: 50px; top: 1130px; font-size: 28px; line-height: 33px; }
  .topics {
    position: absolute; left: 50px; top: 1204px; width: 620px;
    list-style: none; display: grid; grid-template-columns: 300px 300px;
    grid-auto-flow: column; grid-template-rows: repeat(4, 47px);
    font-size: 27px;
  }
  .topics li { display: flex; align-items: center; gap: 14px; }
  .topic-icon {
    width: 20px; height: 20px; border-radius: 50%; flex: none;
    background: radial-gradient(circle at 35% 35%, var(--white) 15%, var(--teal-light) 45%, var(--blue) 100%);
  }
  .voices {
    position: absolute; left: 651px; top: 1156px; width: 525px; height: 338px;
    background: var(--white); border-radius: 0 46px 0 46px;
    padding: 34px 26px 0 30px; font-size: 22px; line-height: 26px;
  }
  .voices-label {
    position: absolute; left: 162px; top: -16px;
    background: var(--blue); color: var(--white);
    font-size: 22px; padding: 2px 18px; border-radius: 8px 8px 0 0;
  }
  .voices p { text-align: justify; }
  .voices .signature { text-align: right; margin: 2px 0 12px; }
  .quote-mark {
    position: absolute; font-size: 130px; line-height: 1; color: var(--teal); font-weight: 700;
  }
  .quote-open { left: 640px; top: 1096px; }
  .quote-close { left: 1082px; top: 1440px; }
  .contact { position: absolute; left: 50px; top: 1494px; color: var(--white); }
  .contact-title { font-size: 25px; font-weight: 700; margin-bottom: 8px; }
  .contact ul { list-style: none; }
  .contact li { display: flex; align-items: center; gap: 18px; font-size: 24px; height: 34px; }
  .contact svg { width: 20px; height: 20px; flex: none; }
</style>
</head>
<body>
<main class="flyer">
  <svg class="flyer-backdrop" viewBox="0 0 1200 1696" aria-hidden="true">
    <defs>
      <linearGradient id="skyGrad" x1="0" y1="0" x2="0" y2="1">
        <stop offset="0" stop-color="#eef8fd"/>
        <stop offset="1" stop-color="#b7e0f4"/>
      </linearGradient>
      <linearGradient id="silverGrad" x1="0" y1="0" x2="1" y2="1">
        <stop offset="0" stop-color="#d9dde1"/>
        <stop offset="0.45" stop-color="#ffffff"/>
        <stop offset="1" stop-color="#dde1e5"/>
      </linearGradient>
      <linearGradient id="bandGrad" x1="0" y1="0" x2="0" y2="1">
        <stop offset="0" stop-color="#1f7bc4"/>
        <stop offset="1" stop-color="#1560a6"/>
      </linearGradient>
    </defs>
    <rect width="1200" height="1696" fill="url(#skyGrad)"/>
    <path d="M0 0 H1200 V360 C900 340 500 330 0 430 Z" fill="url(#silverGrad)"/>
    <path d="M0 440 C250 370 520 360 740 430" fill="none" stroke="#1b70bb" stroke-width="16"/>
    <path d="M0 470 C260 410 520 400 720 460" fill="none" stroke="#8ccdec" stroke-width="6"/>
    <g fill="none" stroke="#8fd0ee" stroke-width="2" opacity="0.8">
      <path d="M0 860 C300 760 700 780 1200 640"/>
      <path d="M0 900 C320 800 720 820 1200 680"/>
      <path d="M0 940 C340 840 740 860 1200 720"/>
      <path d="M200 1000 C500 900 800 900 1200 790"/>
      <path d="M300 1060 C600 960 880 960 1200 860"/>
    </g>
    <path d="M760 650 C900 610 1060 560 1200 540 V580 C1060 600 920 660 780 700 Z" fill="#1b9fa5"/>
    <path d="M780 700 C920 660 1060 610 1200 590 V610 C1060 630 920 690 790 725 Z" fill="#1b70bb" opacity="0.7"/>
    <circle cx="892" cy="262" r="380" fill="#1b70bb"/>
    <circle cx="918" cy="250" r="366" fill="#ffffff"/>
    <path d="M0 1420 C300 1360 620 1470 1200 1400 V1696 H0 Z" fill="#2aa9a7"/>
    <path d="M0 1440 C300 1390 640 1500 1200 1428 V1696 H0 Z" fill="url(#bandGrad)"/>
  </svg>

  <svg class="flyer-backdrop" viewBox="0 0 1200 1696">
    <defs>
      <linearGradient id="portraitGrad" x1="0" y1="0" x2="0" y2="1">
        <stop offset="0" stop-color="#f3f1ee"/>
        <stop offset="0.55" stop-color="#e9d2c2"/>
        <stop offset="1" stop-color="#cfc9c4"/>
      </linearGradient>
      <linearGradient id="roomGrad" x1="0" y1="0" x2="1" y2="1">
        <stop offset="0" stop-color="#d8c6a8"/>
        <stop offset="1" stop-color="#8fa6a8"/>
      </linearGradient>
    </defs>
    <circle cx="918" cy="250" r="356" fill="url(#portraitGrad)" role="img" aria-label="Portrait photo of the counsellor smiling, wearing a white blouse and red scarf"/>
    <circle cx="722" cy="606" r="106" fill="#1b70bb"/>
    <circle cx="722" cy="606" r="98" fill="url(#roomGrad)" role="img" aria-label="Photo of a counselling session around a table"/>
    <circle cx="948" cy="720" r="116" fill="#1b70bb"/>
    <circle cx="948" cy="720" r="108" fill="url(#roomGrad)" role="img" aria-label="Photo of a group seated in the counselling room"/>
  </svg>

  <div class="brand">
    <div class="brand-dot"></div>
    <div class="brand-name">Brigitte Volkanter</div>
    <div class="brand-tag">Familienberatung Donaufeld</div>
  </div>

  <h1 class="headline">I accompany<br>you on your<br>journey</h1>
  <p class="lead">It is never too early and rarely too late to make changes that have a positive effect on your life.</p>

  <h2 class="section-title about-title">About Me</h2>
  <p class="about-text">Accompanying people in their development ...<br>Attention, peace and serenity ...<br>Clear structures and a properly understood approach to discipline ...</p>

  <h2 class="section-title respect-title">Respect and appreciation in working with my clients are very important to me.</h2>
  <p class="topics-intro">Counselling can be offered on<br>a variety of topics, such as:</p>
  <ul class="topics">
    <li><span class="topic-icon"></span>Family systems</li>
    <li><span class="topic-icon"></span>Professional systems</li>
    <li><span class="topic-icon"></span>Body and health</li>
    <li><span class="topic-icon"></span>Symptoms</li>
    <li><span class="topic-icon"></span>Decisions</li>
    <li><span class="topic-icon"></span>Aims</li>
    <li><span class="topic-icon"></span>Resources</li>
    <li><span class="topic-icon"></span>And much more.</li>
  </ul>

  <section class="voices">
    <span class="voices-label">Voices of clients</span>
    <p>Brigitte Volkanter is characterized by warmth, sovereignty, calm and care. Safe and loving, she accompanies you through the process. She is neutral, but interested. You feel well cared for, even if it is "taken care of".</p>
    <p class="signature">Mrs. R. client</p>
    <p>My way was full of stones and wood. I took the broom in the hand and returned. Mrs. Volkanter accompanied me.</p>
    <p class="signature">Mrs. H. client</p>
  </section>
  <span class="quote-mark quote-open">“</span>
  <span class="quote-mark quote-close">”</span>

  <section class="contact">
    <h3 class="contact-title">Contact Info</h3>
    <ul>
      <li><svg viewBox="0 0 20 20"><path d="M10 1a6 6 0 0 0-6 6c0 5 6 12 6 12s6-7 6-12a6 6 0 0 0-6-6zm0 8.5A2.5 2.5 0 1 1 10 4.5a2.5 2.5 0 0 1 0 5z" fill="#fff"/></svg>Lindengasse 14/3, 1220 Vienna</li>
      <li><svg viewBox="0 0 20 20"><rect x="1" y="4" width="18" height="12" fill="#fff"/><path d="M1 4l9 7 9-7" fill="none" stroke="#1b70bb" stroke-width="1.6"/></svg>familienberatung@brigitte-volkanter.at</li>
      <li><svg viewBox="0 0 20 20"><path d="M2 7c0-3 4-4 8-4s8 1 8 4l-3 1-1-2H6L5 8zM5 10h10l2 7H3z" fill="#fff"/><circle cx="10" cy="13" r="2" fill="#1b70bb"/></svg>+43 676 418 25 90</li>
      <li><svg viewBox="0 0 20 20"><circle cx="10" cy="10" r="8.5" fill="#fff"/><path d="M1.5 10h17M10 1.5c-4 4-4 13 0 17M10 1.5c4 4 4 13 0 17" fill="none" stroke="#1b70bb" stroke-width="1.2"/></svg>www.brigitte-volkanter.at</li>
    </ul>
  </section>
</main>
</body>
</html>
```